Magazine advertisement

I need a company advertisement for magazine prints. I need to be able to scale it to different sizes if need be. I need it to showcase our brand, VornaDrive have our phone number 582.463.9047 our contact email address sales@vornadrive.net and web address www.vornadrive.net

Target Market(s)

automotive / tractor pulling

Industry/Entity Type

automotive / racing

Colors
EB3D1F
EC4F4E
F09395
F8D3D4
FCEDEE

Requirements
Must have
• our logo, our color scheme (pantone red 1795, white, black, silver

```html
<!DOCTYPE html>
<html lang="en">
<head>
<meta charset="utf-8">
<title>VornaDrive Magazine Advertisement</title>
<link href="https://fonts.googleapis.com/css2?family=Poppins:wght@400;500;600;700&family=Russo+One&display=swap" rel="stylesheet">
<style>
  :root {
    --red: #EB3D1F;
    --red-bright: #E0252B;
    --red-soft: #EC4F4E;
    --pink: #F09395;
    --blush: #F8D3D4;
    --mist: #FCEDEE;
    --black: #111111;
    --ink: #1a1a1a;
    --silver: #b9bcc0;
    --steel: #6f7377;
    --white: #ffffff;
    --stage: #6b6b6b;
  }
  * { box-sizing: border-box; margin: 0; padding: 0; }
  html, body { width: 1200px; height: 495px; overflow: hidden; background: var(--stage); }
  .canvas { position: relative; width: 1200px; height: 495px; }
  .ad {
    position: absolute; left: 414px; top: 7px; width: 372px; height: 482px;
    overflow: hidden; background: var(--white);
    font-family: "Poppins", sans-serif;
    box-shadow: 0 4px 14px rgba(0,0,0,.35);
  }
  .ad-backdrop { position: absolute; inset: 0; width: 100%; height: 100%; }
  .hero-image {
    position: absolute; left: 22px; top: 188px; width: 340px; height: 270px;
    background: radial-gradient(ellipse at 55% 45%, #d9dadc 0%, #a9acb0 28%, #c7332d 52%, rgba(120,20,20,.5) 68%, rgba(0,0,0,0) 78%);
  }
  .brand {
    position: absolute; top: 46px; left: 0; width: 100%;
    display: flex; align-items: center; justify-content: center; gap: 8px;
  }
  .brand-mark { width: 16px; height: 16px; background: var(--red-bright); }
  .brand-name { font-weight: 700; font-size: 27px; color: var(--red-bright); letter-spacing: 1px; line-height: 1; }
  .headline {
    position: absolute; top: 100px; left: 0; width: 100%; text-align: center;
    font-family: "Russo One", sans-serif; font-size: 20.5px; line-height: 21px;
    color: var(--black); letter-spacing: .6px; text-transform: uppercase;
  }
  .tagline {
    position: absolute; top: 153px; left: 40px; width: 292px; text-align: center;
    font-weight: 600; font-size: 8.6px; line-height: 10.5px; color: var(--red-bright);
  }
  .feature { position: absolute; top: 210px; color: var(--white); z-index: 2; }
  .feature h2 { font-weight: 600; font-size: 8.4px; margin-bottom: 2px; }
  .feature p { font-size: 6.6px; line-height: 8.1px; }
  .feature--left { left: 17px; width: 80px; }
  .feature--right { right: 17px; width: 86px; text-align: right; }
  .contact-bar {
    position: absolute; top: 456px; left: 0; width: 100%; height: 16px;
    display: flex; align-items: center; justify-content: center; gap: 16px;
    background: linear-gradient(90deg, rgba(140,140,140,.8) 0%, rgba(0,0,0,0) 12%, rgba(0,0,0,0) 88%, rgba(140,140,140,.8) 100%);
    color: var(--white); z-index: 2;
  }
  .contact { display: flex; align-items: center; gap: 4px; font-size: 7.2px; font-weight: 500; }
  .contact--phone { font-size: 9.6px; }
  .contact svg { width: 7px; height: 7px; fill: var(--red-bright); }
</style>
</head>
<body>
<main class="canvas">
  <article class="ad">
    <svg class="ad-backdrop" viewBox="0 0 372 482" preserveAspectRatio="none" aria-hidden="true">
      <defs>
        <linearGradient id="sky" x1="0" y1="0" x2="1" y2="1">
          <stop offset="0" stop-color="#ffffff"/>
          <stop offset=".5" stop-color="#FCEDEE"/>
          <stop offset="1" stop-color="#F09395"/>
        </linearGradient>
        <linearGradient id="band" x1="0" y1="0" x2="0" y2="1">
          <stop offset="0" stop-color="#d81f26"/>
          <stop offset=".45" stop-color="#9c1419"/>
          <stop offset="1" stop-color="#111111"/>
        </linearGradient>
        <linearGradient id="wedge" x1="0" y1="0" x2="1" y2="1">
          <stop offset="0" stop-color="#ffffff"/>
          <stop offset="1" stop-color="#9a9da1"/>
        </linearGradient>
      </defs>
      <rect width="372" height="201" fill="url(#sky)"/>
      <rect y="0" width="372" height="3" fill="#E0252B"/>
      <rect x="0" y="184" width="74" height="2" fill="#E0252B"/>
      <rect x="300" y="34" width="72" height="1.5" fill="#c9cbce"/>
      <rect x="310" y="40" width="62" height="1.5" fill="#c9cbce"/>
      <rect y="201" width="372" height="281" fill="url(#band)"/>
      <polygon points="0,400 0,470 372,470 372,378 300,440" fill="#111111"/>
      <polygon points="0,372 120,322 0,470" fill="#E0252B"/>
      <polygon points="0,430 120,322 40,470 0,470" fill="#f2f2f2"/>
      <polygon points="372,400 250,328 372,460" fill="url(#wedge)"/>
      <rect y="470" width="372" height="12" fill="#0b0b0b"/>
    </svg>

    <div class="hero-image" role="img" aria-label="Photo of a polished silver turbocharger above a red pulling tractor charging forward"></div>

    <div class="brand">
      <span class="brand-mark"></span>
      <span class="brand-name">VornaDrive</span>
    </div>

    <h1 class="headline">Maximum Performance<br>Ultimate Power</h1>
    <p class="tagline">Specializing in high-performance turbochargers for automotive racing and tractor pulling.</p>

    <section class="feature feature--left">
      <h2>Built to Win</h2>
      <p>We’ll help you perform like a winner, from truck and tractor pulling to drag racing. Our turbochargers are equipped with the capacity to power everything from high-end sports cars to snowmobiles.</p>
    </section>

    <section class="feature feature--right">
      <h2>One Fierce Turbine</h2>
      <p>Our hub-free design maximizes aerodynamics and has been dyno-proven to yield maximum horsepower without the need to increase frame size.</p>
    </section>

    <footer class="contact-bar">
      <span class="contact contact--phone">
        <svg viewBox="0 0 24 24"><path d="M6.6 10.8a15 15 0 0 0 6.6 6.6l2.2-2.2a1 1 0 0 1 1-.25 11.4 11.4 0 0 0 3.6.57 1 1 0 0 1 1 1V20a1 1 0 0 1-1 1A17 17 0 0 1 3 4a1 1 0 0 1 1-1h3.5a1 1 0 0 1 1 1c0 1.25.2 2.45.57 3.57a1 1 0 0 1-.25 1z"/></svg>
        582.463.9047
      </span>
      <span class="contact">
        <svg viewBox="0 0 24 24"><path d="M2 5h20v14H2z M4 7v.5l8 5 8-5V7l-8 5z" fill-rule="evenodd"/></svg>
        sales@vornadrive.net
      </span>
      <span class="contact">
        <svg viewBox="0 0 24 24"><path d="M12 2a10 10 0 1 0 0 20 10 10 0 0 0 0-20zm6.9 9h-3a15 15 0 0 0-1.4-6A8 8 0 0 1 18.9 11zM12 4.1A13 13 0 0 1 13.9 11h-3.8A13 13 0 0 1 12 4.1zM9.5 5a15 15 0 0 0-1.4 6h-3A8 8 0 0 1 9.5 5zM5.1 13h3a15 15 0 0 0 1.4 6A8 8 0 0 1 5.1 13zm6.9 6.9A13 13 0 0 1 10.1 13h3.8A13 13 0 0 1 12 19.9zm2.5-.9a15 15 0 0 0 1.4-6h3a8 8 0 0 1-4.4 6z"/></svg>
        www.vornadrive.net
      </span>
    </footer>
  </article>
</main>
</body>
</html>
```